Specialized tax accounting firm needs marketing postcard

We need a postcard design for a professional services firm called R. Desmond Plork Inc. The firm is essentially a very specialized tax accounting firm - instead of serving the end consumer, we support other public accounting firms in the area of Canadian and U.S. tax advisory and compliance (i.e. they call us on tax issues too complex for the general practitioner). Our byline is "Tax Support Services for Public Accounting Firms". Our postcard should utilize our logo and be based on colours present in our logo (see file attached). The final design needs to convey professionalism and trustworthiness (we're hired by accountants after all!) while being creative and eye-catching. Eye-catching is critical, since many prospective recipients will not have heard from me before and I want them to read the postcard.

I've attached:
The font used in the logo
The logo itself in a variety of file formats
A picture of myself for incorporation in the postcard
A sample postcard from Publisher showing the wording to be used in the postcard and the elements to be included

Please note that in including a draft postcard I don't want the designer to follow the layout as is. It just shows the basic elements I want included. The only element which should remain constant is the wording - I do want the text elements included as written - however, everything else - font, size, placement of elements, etc. is up for creative ideas.

Please note that there is much more leather background around the logo than needs to be incorporated in the letterhead.

Industry/Entity Type

Accounting

```html
<!DOCTYPE html>
<html lang="en">
<head>
<meta charset="utf-8">
<title>R. Desmond Plork Inc. — Postcard</title>
<link href="https://fonts.googleapis.com/css2?family=Cinzel:wght@400;600;700&family=Source+Sans+3:wght@400&display=swap" rel="stylesheet">
<style>
  :root {
    --card-white: #fbfbfa;
    --backdrop-dark: #1f1f1f;
    --backdrop-mid: #3a3a3a;
    --leather-light: #3a3836;
    --leather-mid: #242322;
    --leather-dark: #121212;
    --cream: #f4ecd8;
    --body-text: #eeece8;
    --gold: #d2ad63;
    --logo-square: #c9a35a;
    --photo-warm: #8c7566;
    --photo-grey: #4d4d4f;
    --photo-suit: #1c1d21;
  }
  * { margin: 0; padding: 0; box-sizing: border-box; }
  html, body {
    width: 1200px;
    height: 948px;
    overflow: hidden;
    background: var(--card-white);
  }
  .postcard {
    position: relative;
    width: 1200px;
    height: 948px;
    background: var(--card-white);
    overflow: hidden;
  }
  .backdrop {
    position: absolute;
    left: 42px;
    top: 43px;
    width: 1116px;
    height: 860px;
    background: linear-gradient(90deg, var(--backdrop-dark) 0%, var(--backdrop-mid) 70%, #2a2a2a 100%);
  }
  .portrait {
    position: absolute;
    left: 699px;
    top: 43px;
    width: 459px;
    height: 860px;
    background:
      radial-gradient(ellipse 38% 20% at 52% 27%, rgba(150,124,106,0.9) 0%, rgba(140,117,102,0.45) 55%, rgba(140,117,102,0) 100%),
      linear-gradient(180deg, rgba(28,29,33,0) 0%, rgba(28,29,33,0) 36%, rgba(28,29,33,0.85) 52%, var(--photo-suit) 100%),
      radial-gradient(ellipse at 50% 35%, #5c5c5e 0%, var(--photo-grey) 45%, #2e2e30 100%);
  }
  .portrait-name {
    position: absolute;
    left: 699px;
    top: 836px;
    width: 459px;
    text-align: center;
    font-family: "Cinzel", serif;
    font-weight: 700;
    font-size: 31px;
    line-height: 40px;
    color: #ffffff;
    white-space: nowrap;
  }
  .leather-panel {
    position: absolute;
    left: 75px;
    top: 0;
    width: 612px;
    height: 948px;
    background:
      radial-gradient(ellipse at 45% 38%, var(--leather-light) 0%, var(--leather-mid) 55%, var(--leather-dark) 100%);
    box-shadow: 5px 0 14px rgba(0,0,0,0.5);
  }
  .fold {
    position: absolute;
    left: 687px;
    width: 40px;
    height: 40px;
  }
  .fold-top { top: 0; }
  .fold-bottom { bottom: 0; }
  .brand {
    position: absolute;
    left: 100px;
    top: 50px;
    width: 570px;
    display: flex;
    align-items: flex-start;
    gap: 14px;
  }
  .brand-square {
    width: 78px;
    height: 78px;
    background: var(--logo-square);
    flex: none;
  }
  .brand-text {
    display: flex;
    flex-direction: column;
    align-items: center;
    width: 478px;
  }
  .brand-name {
    font-family: "Cinzel", serif;
    font-weight: 400;
    font-size: 40px;
    line-height: 44px;
    letter-spacing: 1px;
    color: #ffffff;
    white-space: nowrap;
  }
  .brand-suffix {
    display: flex;
    align-items: center;
    gap: 8px;
    width: 100%;
    font-family: "Cinzel", serif;
    font-size: 12px;
    line-height: 14px;
    letter-spacing: 2px;
    color: #ffffff;
  }
  .brand-suffix::before, .brand-suffix::after {
    content: "";
    flex: 1;
    height: 1px;
    background: rgba(255,255,255,0.6);
  }
  .brand-byline {
    margin-top: 4px;
    font-family: "Cinzel", serif;
    font-size: 13px;
    letter-spacing: 0.4px;
    color: #ffffff;
    white-space: nowrap;
  }
  .headline {
    position: absolute;
    left: 100px;
    top: 164px;
    width: 570px;
    text-align: center;
    font-family: "Cinzel", serif;
    font-weight: 700;
    font-size: 31px;
    line-height: 53px;
    color: var(--cream);
  }
  .body-copy {
    position: absolute;
    left: 156px;
    width: 502px;
    font-family: "Source Sans 3", sans-serif;
    font-size: 26px;
    line-height: 33.6px;
    color: var(--body-text);
  }
  .body-copy .line {
    display: block;
    white-space: nowrap;
    text-align: justify;
    text-align-last: justify;
  }
  .body-copy .line.last {
    text-align: left;
    text-align-last: left;
  }
  .copy-intro { top: 283px; }
  .copy-pitch { top: 502px; }
  .copy-close { top: 787px; }
</style>
</head>
<body>
  <main class="postcard">
    <div class="backdrop"></div>
    <div class="portrait" role="img" aria-label="Portrait photograph of the accountant in a dark suit and tie, arms crossed, against a grey studio backdrop"></div>
    <p class="portrait-name">Rowan D. Plork, CGA</p>

    <section class="leather-panel" aria-label="Message"></section>
    <svg class="fold fold-top" viewBox="0 0 40 40" aria-hidden="true">
      <polygon points="0,0 40,0 0,40" fill="#0e0e0e"/>
    </svg>
    <svg class="fold fold-bottom" viewBox="0 0 40 40" aria-hidden="true">
      <polygon points="0,0 40,40 0,40" fill="#0e0e0e"/>
    </svg>

    <header class="brand">
      <div class="brand-square"></div>
      <div class="brand-text">
        <span class="brand-name">R. DESMOND PLORK</span>
        <span class="brand-suffix">INC</span>
        <span class="brand-byline">TAX SUPPORT SERVICES FOR PUBLIC ACCOUNTING FIRMS</span>
      </div>
    </header>

    <h1 class="headline">Do your clients need help<br>with their U.S. taxes?</h1>

    <p class="body-copy copy-intro">
      <span class="line">You probably know that U.S. citizens have</span>
      <span class="line">to file U.S. tax returns every year—even if</span>
      <span class="line">they live in Canada. So do your clients.</span>
      <span class="line">That’s why they’re asking you if you know</span>
      <span class="line">anyone who can help them with their U.S.</span>
      <span class="line last">filings.</span>
    </p>

    <p class="body-copy copy-pitch">
      <span class="line">Finding a tax accountant who can help</span>
      <span class="line">with U.S. filings is tough. U.S. tax preparers</span>
      <span class="line">have to be registered with the IRS to be</span>
      <span class="line">eligible to prepare U.S. returns. Your client</span>
      <span class="line">needs someone with experience,</span>
      <span class="line">someone timely, someone charging a</span>
      <span class="line">reasonable price. With a proven track</span>
      <span class="line last">record of over 15 years, I can deliver.</span>
    </p>

    <p class="body-copy copy-close">
      <span class="line">Feel free to pass along my contact</span>
      <span class="line">information to your clients. I’d be glad to</span>
      <span class="line last">chat.</span>
    </p>
  </main>
</body>
</html>
```